Tempered Glass Screen Protector Label Design

The Label design is for a NO brand company, so there will be no logo.

Our main products are all type of Screen protector for Smartphone and tablet computer. For this label design would focusing on ‘Tempered Glass Screen Protector’ can be reference to http://www.vextalo.example/en

The label layout is been giving in resources files; there will be 3 different sizes, there all need same design; the packaging itself will be all transparent unlike in the image. I have taken several example of packaging label [image (1)-(3)] what it would be like insert in the packaging.

The design should be neat and simple but also have a strong feeling at the same time. The color is up to all designer to decide.

The front label should have a smartphone an Zorvex5 for the smallest size packaging label layout, an Lumtab mini for the medium size and an Lumtab for the large size. Text to put on the cover :“Premium Tempered Glass Screen Protector”

The back label will be about the characteristic of the product.
The back label should have an icon of
-9H hardness
-oleophobic coating
-Delicate Touch
-Anti-fingerprint
-High Definition [HD]
-Shock resistance

Note* Please make an icon ”Materials from Japan”
Updates

Target Market(s)

Small distributor company, mobile accessories shop in the mall.

Industry/Entity Type

Computer

Font styles to use
Serif
Sans Serif
Other font styles liked:
• innovation technology style fonts

Colors

Designer to choose colors to be used in the design.

Requirements
Must have
• design should be simple but Strong and Unique.

```html
<!DOCTYPE html>
<html lang="en">
<head>
<meta charset="utf-8">
<title>Premium Tempered Glass Screen Protector – Label</title>
<link href="https://fonts.googleapis.com/css2?family=Teko:wght@300;400;600&family=Open+Sans:wght@400;600&family=Saira+Condensed:wght@800&display=swap" rel="stylesheet">
<style>
  :root{
    --bg:#ececf0;
    --ink:#2a2a2a;
    --panel:#000000;
    --panel-soft:#2b2b2b;
    --text:#ffffff;
    --lime:#b6f21a;
    --pink:#ff3f6b;
    --red:#ff1446;
    --orange:#f2542d;
    --blue:#1aa3e8;
    --cyan:#1ec8f5;
    --print:#a01818;
  }
  *{margin:0;padding:0;box-sizing:border-box}
  html,body{width:1200px;height:675px;overflow:hidden;background:var(--bg)}
  .canvas{position:relative;width:1200px;height:675px;overflow:hidden;background:var(--bg)}

  .headline{position:absolute;left:510px;top:32px;width:200px;text-align:center;color:var(--ink);
    font-family:"Saira Condensed",sans-serif;font-weight:800;line-height:1}
  .headline .main{font-size:29px;letter-spacing:.2px}
  .headline .sub{font-size:14px;margin-top:2px}

  .label{position:absolute;background:var(--panel);color:var(--text);font-family:"Open Sans",sans-serif}
  .label .title{font-family:"Teko",sans-serif;font-weight:400;text-align:center;line-height:.9;text-transform:uppercase}
  .label .title .main{font-size:1.6em;letter-spacing:.02em}
  .label .title .sub{font-size:.85em;letter-spacing:.04em}
  .features{list-style:none;margin-left:var(--indent)}
  .feature{display:flex;align-items:center;height:var(--row)}
  .feature .icon{width:3em;display:flex;align-items:center;justify-content:flex-start}
  .feature .icon svg{width:2.4em;height:2.4em}
  .feature .name{font-size:1em}
  .badge{font-family:"Open Sans",sans-serif;font-weight:600;font-size:2.1em;line-height:1}
  .badge.hard{color:var(--lime)}
  .badge.hd{color:var(--red);font-style:italic;font-weight:600}
  .print{width:1.8em;height:2.5em;border-radius:50%;background:radial-gradient(circle at 45% 40%,#c22a2a,var(--print) 70%)}

  .label.phone{left:119px;top:114px;width:241px;height:413px;font-size:13px;--indent:40px;--row:52px;padding-top:68px}
  .label.phone .title{margin-bottom:6px}

  .card-back{position:absolute;left:514px;top:148px;width:220px;height:353px;background:rgba(255,255,255,.45)}
  .label.card{left:489px;top:170px;width:221px;height:350px;font-size:11.5px;--indent:33px;--row:46px;padding-top:28px;
    background:linear-gradient(160deg,#1d1d1d,var(--panel-soft) 60%,#333);box-shadow:0 8px 16px rgba(0,0,0,.35)}
  .label.card .title .main{font-weight:600}
  .label.card .title{margin-bottom:8px}
  .label.card .badge.hd{color:var(--orange)}

  .label.tablet{left:786px;top:145px;width:414px;height:530px;font-size:17px;--indent:118px;--row:66px;padding-top:28px}
  .label.tablet .title{margin-bottom:4px;padding-right:10px}
</style>
</head>
<body>
<main class="canvas">
  <header class="headline">
    <div class="main">PREMIUM TEMPERED</div>
    <div class="sub">GLASS SCREEN PROTECTOR</div>
  </header>

  <section class="label phone">
    <div class="title"><div class="main">Premium Tempered</div><div class="sub">Glass Screen Protector</div></div>
    <ul class="features">
      <li class="feature"><span class="icon"><span class="badge hard">9H</span></span><span class="name">Hardness</span></li>
      <li class="feature"><span class="icon"><svg viewBox="0 0 40 30"><path d="M10 4h26l-8 7H2z" fill="#ff7f9a"/><path d="M10 11h26l-8 7H2z" fill="#ff5a7e"/><path d="M10 18h26l-8 7H2z" fill="var(--pink)"/></svg></span><span class="name">Oleophobic Coating</span></li>
      <li class="feature"><span class="icon"><svg viewBox="0 0 40 30"><rect x="4" y="4" width="28" height="20" rx="2" fill="none" stroke="var(--blue)" stroke-width="3"/><path d="M10 18l5-6 4 3 6-7" fill="none" stroke="var(--blue)" stroke-width="2"/><path d="M24 16v10h8l2-6-6-2v-2z" fill="var(--blue)"/></svg></span><span class="name">Delicate Touch</span></li>
      <li class="feature"><span class="icon"><span class="print" role="img" aria-label="red fingerprint icon"></span></span><span class="name">Anti-fingerprint</span></li>
      <li class="feature"><span class="icon"><span class="badge hd">HD</span></span><span class="name">High Definition</span></li>
      <li class="feature"><span class="icon"><svg viewBox="0 0 40 34"><path d="M8 16a10 10 0 0 1 14-10" fill="none" stroke="var(--cyan)" stroke-width="4"/><path d="M20 1l6 5-6 5z" fill="var(--cyan)"/><path d="M32 18a10 10 0 0 1-14 10" fill="none" stroke="var(--cyan)" stroke-width="4"/><path d="M20 33l-6-5 6-5z" fill="var(--cyan)"/><path d="M21 10l-4 7h5l-3 7" fill="none" stroke="var(--cyan)" stroke-width="2"/></svg></span><span class="name">Shock resistance</span></li>
    </ul>
  </section>

  <div class="card-back"></div>
  <section class="label card">
    <div class="title"><div class="main">Premium Tempered</div><div class="sub">Glass Screen Protector</div></div>
    <ul class="features">
      <li class="feature"><span class="icon"><span class="badge hard">9H</span></span><span class="name">Hardness</span></li>
      <li class="feature"><span class="icon"><svg viewBox="0 0 40 30"><path d="M10 4h26l-8 7H2z" fill="#ff7f9a"/><path d="M10 11h26l-8 7H2z" fill="#ff5a7e"/><path d="M10 18h26l-8 7H2z" fill="var(--pink)"/></svg></span><span class="name">Oleophobic Coating</span></li>
      <li class="feature"><span class="icon"><svg viewBox="0 0 40 30"><rect x="4" y="4" width="28" height="20" rx="2" fill="none" stroke="var(--blue)" stroke-width="3"/><path d="M10 18l5-6 4 3 6-7" fill="none" stroke="var(--blue)" stroke-width="2"/><path d="M24 16v10h8l2-6-6-2v-2z" fill="var(--blue)"/></svg></span><span class="name">Delicate Touch</span></li>
      <li class="feature"><span class="icon"><span class="print" role="img" aria-label="red fingerprint icon"></span></span><span class="name">Anti-fingerprint</span></li>
      <li class="feature"><span class="icon"><span class="badge hd">HD</span></span><span class="name">High Definition</span></li>
      <li class="feature"><span class="icon"><svg viewBox="0 0 40 34"><path d="M8 16a10 10 0 0 1 14-10" fill="none" stroke="var(--cyan)" stroke-width="4"/><path d="M20 1l6 5-6 5z" fill="var(--cyan)"/><path d="M32 18a10 10 0 0 1-14 10" fill="none" stroke="var(--cyan)" stroke-width="4"/><path d="M20 33l-6-5 6-5z" fill="var(--cyan)"/><path d="M21 10l-4 7h5l-3 7" fill="none" stroke="var(--cyan)" stroke-width="2"/></svg></span><span class="name">Shock resistance</span></li>
    </ul>
  </section>

  <section class="label tablet">
    <div class="title"><div class="main">Premium Tempered</div><div class="sub">Glass Screen Protector</div></div>
    <ul class="features">
      <li class="feature"><span class="icon"><span class="badge hard">9H</span></span><span class="name">Hardness</span></li>
      <li class="feature"><span class="icon"><svg viewBox="0 0 40 30"><path d="M10 4h26l-8 7H2z" fill="#ff7f9a"/><path d="M10 11h26l-8 7H2z" fill="#ff5a7e"/><path d="M10 18h26l-8 7H2z" fill="var(--pink)"/></svg></span><span class="name">Oleophobic Coating</span></li>
      <li class="feature"><span class="icon"><svg viewBox="0 0 40 30"><rect x="4" y="4" width="28" height="20" rx="2" fill="none" stroke="var(--blue)" stroke-width="3"/><path d="M10 18l5-6 4 3 6-7" fill="none" stroke="var(--blue)" stroke-width="2"/><path d="M24 16v10h8l2-6-6-2v-2z" fill="var(--blue)"/></svg></span><span class="name">Delicate Touch</span></li>
      <li class="feature"><span class="icon"><span class="print" role="img" aria-label="red fingerprint icon"></span></span><span class="name">Anti-fingerprint</span></li>
      <li class="feature"><span class="icon"><span class="badge hd">HD</span></span><span class="name">High Definition</span></li>
      <li class="feature"><span class="icon"><svg viewBox="0 0 40 34"><path d="M8 16a10 10 0 0 1 14-10" fill="none" stroke="var(--cyan)" stroke-width="4"/><path d="M20 1l6 5-6 5z" fill="var(--cyan)"/><path d="M32 18a10 10 0 0 1-14 10" fill="none" stroke="var(--cyan)" stroke-width="4"/><path d="M20 33l-6-5 6-5z" fill="var(--cyan)"/><path d="M21 10l-4 7h5l-3 7" fill="none" stroke="var(--cyan)" stroke-width="2"/></svg></span><span class="name">Shock resistance</span></li>
    </ul>
  </section>
</main>
</body>
</html>
```